Tall-Anchor Brochure

We would like a 3 panel layout format with copy on both sides and on each panel, (we will provide content).

We are Tall-Anchor and we work with business owners to achieve measurable growth and success based on 6 Core Pillars Of Momentum and (S.B.L) 90 Day Steady Build Ledger. We also work with the business leader and individuals within the organization with personal development.

We would like the brochure to have a corporate feel, but warm and inviting. We don't want a hard or aggressive feel.

We would like it to be available for pdf upload and physical print formats.

The winning design will also be invited to design a header for our website as well. The header will be consistent with the brochure, so please keep that in mind during your creative process.

I am enclosing a transparent copy of our company logo along with content for the brochure.

Thank you in advance for your consideration!

Gordon and Moira
Updates

Sorry, but we forgot to include the front cover text.

It will read as follows,

Do you know The 6 Core Pillars of Momentum  that are crucial to the success of any business today?

Also, please add the following to the back page

Website: www.tall-anchor.example
Resource Centre: www.taresources.example 
Phone: +44 (0) 7812056417
Email: info@tall-anchor.example

Follow us on (please insert Facebook, Linkedin and YouTube logo)

I have uploaded a pdf format of brochure text.

Hello designers. I wanted to give some further input to help the process. Although the brochure is to target business, we don't want to over do it with corporate professioanls in all the photos. If there is an opportunity to incorporate photos of small business owners like, a butcher, baker, chef, flower shop etc. This would hopefully help us make an immpression to all small business owners.

Thank you, and good luck!

Gordon and Moira  

Reason: A few designers have come come on board last minute. So I'd like to give everyone the same opportunity to respond. Sincerely, Gordon

Target Market(s)

Small Business Owners searching for new ways to grow their business in the UK and Republic Of Ireland.

Industry/Entity Type

Business

```html
<!DOCTYPE html>
<html lang="en">
<head>
<meta charset="utf-8">
<title>Tall-Anchor Brochure – Inside Spread</title>
<link href="https://fonts.googleapis.com/css2?family=Open+Sans:ital,wght@0,400;0,600;0,700;1,400&display=swap" rel="stylesheet">
<style>
  :root {
    --page-bg: #d9d6d3;
    --paper: #f4f4f4;
    --paper-shade: #e4e4e5;
    --band-grey: #707072;
    --band-dark: #5f5f61;
    --ink: #5a5a5c;
    --ink-strong: #4a4a4c;
    --accent: #6a2870;
    --link: #4a58b8;
    --white: #ffffff;
  }
  * { box-sizing: border-box; margin: 0; padding: 0; }
  html, body {
    width: 1200px; height: 960px; overflow: hidden;
    background: var(--page-bg);
    font-family: "Open Sans", Arial, sans-serif;
    color: var(--ink);
  }
  .spread {
    position: absolute; left: 30px; top: 30px;
    width: 1140px; height: 900px;
    background: linear-gradient(180deg, var(--paper-shade) 0%, var(--paper) 45%, var(--white) 100%);
    display: flex;
    box-shadow: 0 6px 18px rgba(0,0,0,.18);
    overflow: hidden;
  }
  .panel {
    position: relative; width: 380px; height: 100%;
    border-right: 1px solid rgba(0,0,0,.06);
  }
  .panel:last-child { border-right: none; }
  .photo { height: 215px; width: 100%; }
  .photo--salon { background: linear-gradient(120deg, #5fbf3a 0%, #9bd66a 35%, #c2473f 55%, #8c8e93 80%, #4f6f9a 100%); }
  .photo--deli { background: linear-gradient(120deg, #7a3b25 0%, #b8693f 30%, #d9a785 55%, #f1efec 75%, #8a5a3a 100%); }
  .photo--cafe { background: linear-gradient(120deg, #b5343c 0%, #d8d2cb 35%, #a8282f 55%, #eae6e2 75%, #7c7a7a 100%); }
  .heading-band {
    position: relative; height: 52px;
    background: linear-gradient(180deg, var(--band-grey), var(--band-dark));
    display: flex; align-items: center; justify-content: center;
  }
  .heading-band::after {
    content: ""; position: absolute; left: 50%; bottom: -10px;
    transform: translateX(-50%);
    border-left: 11px solid transparent; border-right: 11px solid transparent;
    border-top: 10px solid var(--band-dark);
  }
  .heading-band h2 {
    color: var(--white); font-weight: 600; font-size: 18px; letter-spacing: .2px;
  }
  .panel-body { padding: 60px 30px 0 32px; font-size: 12.5px; line-height: 1.55; }
  .panel-body p { margin-bottom: 12px; }
  .panel--intro .panel-body { padding-top: 72px; }
  .panel--start .panel-body { padding-top: 58px; }
  .panel--solutions .panel-body { padding-top: 48px; }
  .link { color: var(--link); font-style: italic; white-space: nowrap; }
  .strong { color: var(--ink-strong); font-weight: 700; }
  .accent { color: var(--accent); font-weight: 700; }
  .subhead { font-size: 14px; font-weight: 700; color: var(--ink-strong); margin: 16px 0 12px; }
  .pillar-list { list-style: none; margin: 6px 0 22px 100px; }
  .pillar-list li::before { content: "-  "; }
  .service-list { list-style: none; margin-top: 16px; }
  .quote {
    position: absolute; left: 30px; right: 16px; top: 710px;
    padding: 8px 10px;
    background: linear-gradient(90deg, rgba(255,255,255,0) 0%, #ffffff 15%, #ffffff 85%, rgba(255,255,255,0) 100%);
    font-weight: 700; font-size: 17px; line-height: 1.4; color: var(--band-dark);
    text-transform: uppercase; text-align: center;
  }
  .brand {
    position: absolute; left: 40px; bottom: 80px;
    display: flex; align-items: center; gap: 10px;
  }
  .brand-mark { width: 22px; height: 22px; background: var(--accent); }
  .brand-name { font-size: 22px; font-weight: 700; color: var(--band-dark); }
  .footer-band { position: absolute; left: 0; bottom: 0; width: 1140px; height: 60px; }
</style>
</head>
<body>
  <main class="spread">
    <section class="panel panel--intro">
      <div class="photo photo--salon" role="img" aria-label="Smiling hair salon owner with arms crossed in a bright green salon, clients seated behind"></div>
      <header class="heading-band"><h2>Helping Your Business</h2></header>
      <div class="panel-body">
        <p>Recently there has been a growing trend in small business owners enlisting outside sources to help them find ways to grow and promote their businesses. At Tall-Anchor we have over 30 years combined experience in management, ownership and consulting in a wide array of businesses. We know what works and what doesn’t, and being entrepreneurs ourselves, we know first hand the struggles that can come with owning a business. Our latest venture saw us grow a new construction company from zero to over 6 MILLION in revenues in just under 2 years. This was achieved through the implementation of our unique sales, marketing and customer service strategies. Our genuine desire to help businesses and individuals succeed is what Tall-Anchor is all about.</p>
      </div>
      <div class="brand">
        <span class="brand-mark"></span>
        <span class="brand-name">Tall-Anchor</span>
      </div>
    </section>

    <section class="panel panel--start">
      <div class="photo photo--deli" role="img" aria-label="Butcher in a white coat standing in front of a delicatessen counter with hanging cured meats"></div>
      <header class="heading-band"><h2>Getting Started</h2></header>
      <div class="panel-body">
        <p>The first step is to visit <span class="link">www.tall-anchor.example</span> or call <span class="strong">07812056417</span> to book your <span class="strong">FREE CONSULTATION</span>. This will be an opportunity for you to think about where you want your business to go and for us to establish how we can help you get there.</p>
        <h3 class="subhead">After That?</h3>
        <p>We will carry out a business analysis based on <span class="accent">The 6 Core Pillars</span> of Momentum:</p>
        <ul class="pillar-list">
          <li>Your Brand</li>
          <li>Sales</li>
          <li>Your People</li>
          <li>Product and Service</li>
          <li>Psychology and Skills</li>
          <li>Finance</li>
        </ul>
        <p>We then provide you with a detailed report and work with you to create and implement your Steady Build Ledger (S.B.L). This is a 90 day plan, customized for your business and designed so you can start seeing positive and measurable results immediately.</p>
      </div>
    </section>

    <section class="panel panel--solutions">
      <div class="photo photo--cafe" role="img" aria-label="Café owner with arms crossed beside a glass pastry counter in a red-walled tearoom"></div>
      <header class="heading-band"><h2>Business Solutions</h2></header>
      <div class="panel-body">
        <p>In addition to the Total Business Analysis / S.B.L package, we also offer other business solutions which can be used individually or bundled together to create a package suitable for your needs.</p>
        <ul class="service-list">
          <li>One on one business mentoring</li>
          <li>Marketing strategies</li>
          <li>Sales training (individual or group)</li>
          <li>Management training (individual or group)</li>
          <li>Customer service training (individual or group)</li>
        </ul>
      </div>
      <p class="quote">“Practical and affordable<br>solutions for any business”</p>
    </section>

    <svg class="footer-band" viewBox="0 0 1140 60" preserveAspectRatio="none" aria-hidden="true">
      <path d="M0 34 Q570 18 1140 12 L1140 60 L0 60 Z" fill="var(--band-grey)"/>
      <path d="M780 20 Q960 10 1140 4 L1140 34 Q960 38 860 46 Z" fill="var(--accent)"/>
    </svg>
  </main>
</body>
</html>
```